Restaurant website built on Plimo’s responsive platform- No coding skills needed

We are looking to add to our company's website www.plimoweb.com a new inspiration page that will include examples of sites built using Plimo's platform.
In order to make it relevant, we would like to have multiple choices for every category, one of the categories is “restaurants.”

REQUIREMENTS:
o Build a "fake" restaurant site on Plimo’s responsive platform, no real restaurant information is needed. The site will include:
1. Homepage
• Restaurant header (no logo)
• Paragraph about the restaurant (can be Lorem ipsum)
• Contact details and contact buttons
• Tastr reviews
• Reserve-a-table widget
• Open hours
2. Menu page
• You can use any menu you'd like
• Reserve a table widget
• Photo gallery
3. Footer
• Social Media links
• Map with location of restaurant

* Order of the elements is up to the designer
* Designer may add more elements as they see fit
* Designer may alter elements from page to page
* Designer will define the site color pallet and text style

****Learn more on how to create a website on Plimo's platform here
https://clipzen.example/584203117

INSTRUCTIONS FOR THIS PROJECT:
Register for a 30-day free trial for Pro access to the platform:
http://www.plimoweb.com/plimopro?_pw_referral=GrfHub

a. After registering, access the dashboard and click on “Create Responsive Website.”
b. Choose a template
c. Start editing! .
d. No need to publish. When ready, take a screenshot of the preview and submit the screenshot to this GraphicHub project. Include the URL/Link to the preview within the submission description.
e. For more information on Plimo, visit the support page at https://support.plimoweb.com/02PlimoOne/Quick_Guide OR call our Support line Mon.-Fri., 9AM-9PM ET.1-866-555-0193

DESIGN PREFERENCES
freestyle (not related to the Plimo brand)

DESIGN SAMPLES (for inspiration)
http://www.plimoweb.com/responsive-website/templates

What not to include in the design -
no restrictions

DELIVERABLES:
* Website on Plimo (No PSD. No coding needed)
* Screenshot preview to GraphicHub with URL/link to your site’s preview.

ABOUT THE COMPANY:
Plimo is a website builder based in California that allow designers, web designers and practically anyone to build its own site. No development and/or technical skills required.

NOTE:
* Plimo is an external site and is not part of GraphicHub
* Please refer to Plimo's Terms and Conditions for information regarding how submissions will be handled (http://www.plimoweb.com/legal/terms)

Target Market(s)

SMBs and web designers that want to create simple, professional and beautiful websites

Industry/Entity Type

Restaurant

Number of Pages Required

2 page

Requirements
Must have
• Please send a preview of the site you created on Plimo, NOT a PSD/JPEG
Should not have
• No coding skills are needed- any web designer can build a site on Plimo

```html
<!DOCTYPE html>
<html lang="en">
<head>
<meta charset="utf-8">
<title>Restaurant</title>
<link rel="stylesheet" href="https://fonts.googleapis.com/css2?family=Source+Sans+Pro:wght@300;400;600;700&family=Open+Sans:wght@400;600;700&display=swap">
<style>
:root{
  --green:#7cbd1e;
  --green-dark:#6aa618;
  --black:#000;
  --ink:#2b2b2b;
  --muted:#555;
  --field:#e6e6e6;
  --footer:#3f3f3f;
  --white:#fff;
  --teal:#4bb9c4;
}
*{box-sizing:border-box;margin:0;padding:0}
html,body{width:1200px;height:4337px;overflow:hidden}
body{position:relative;background:var(--white);font-family:"Open Sans",Arial,sans-serif;color:var(--ink)}
.abs{position:absolute}
.display{font-family:"Source Sans Pro",Arial,sans-serif}

/* header & hero */
.hero{left:0;top:0;width:1200px;height:584px;background:linear-gradient(100deg,#e9ecee 0%,#f7f5f1 40%,#e8dccb 70%,#c68a4a 100%)}
.topbar{left:0;top:0;width:1200px;height:58px;background:rgba(20,20,20,.8)}
.brand{left:152px;top:8px;font-family:"Source Sans Pro",sans-serif;font-size:30px;color:var(--white);font-weight:400}
.social-top{top:21px;width:16px;height:16px;background:var(--white);border-radius:50%}
.hero-title{left:0;width:1200px;top:175px;text-align:center;font-family:"Source Sans Pro",sans-serif;font-size:60px;color:#111}
.hero-lead{left:330px;width:540px;top:264px;text-align:center;font-size:18px;line-height:27px;color:#111}
.btn-dark{left:491px;top:367px;width:220px;height:41px;background:#111;color:var(--white);font-size:17px;display:flex;align-items:center;justify-content:center;gap:14px}

.nav{left:0;top:584px;width:1200px;height:64px;background:var(--green);display:flex;align-items:center}
.nav a{position:absolute;color:var(--white);font-size:15px;font-weight:700;text-decoration:none;transform:translateX(-50%)}

/* about */
.about-title{left:0;width:1200px;top:698px;text-align:center;font-family:"Source Sans Pro",sans-serif;font-size:50px;font-weight:300;color:#333}
.about-title b{font-weight:700}
.about-sub{left:0;width:1200px;top:768px;text-align:center;font-size:22px;color:#333}
.about-text{left:98px;width:1004px;top:826px;text-align:center;font-size:14px;line-height:22px;color:#666}
.btn-green{background:var(--green);color:var(--white);display:flex;align-items:center;justify-content:center;border-radius:3px}
.find{left:515px;top:919px;width:280px;height:52px;font-size:20px}

/* bands */
.band{left:0;width:1200px;display:flex;align-items:center;justify-content:center;font-family:"Source Sans Pro",sans-serif;color:var(--white);font-size:48px;font-weight:300}
.band b{font-weight:700}
.band.black{background:var(--black)}
.band.green{background:var(--green);font-weight:400}

/* menu */
.menu-bg{left:0;top:1107px;width:1200px;height:1067px;background:radial-gradient(ellipse at 70% 60%,#e6c9a8 0%,#f1e3d2 40%,#f8f1ea 75%,#fbf8f4 100%)}
.cat{left:101px;font-family:"Source Sans Pro",sans-serif;font-size:30px;color:#222}
.rule{left:101px;width:960px;height:2px;background:#333}
.item{width:422px}
.item-head{display:flex;justify-content:space-between;color:var(--green);font-size:15px;font-weight:700}
.item-desc{font-size:15px;font-weight:700;line-height:22px;color:#222;width:310px}
.full-menu{left:442px;top:2084px;width:278px;height:44px;font-size:16px;font-weight:600}

.gallery-tile{top:2252px;height:373px;width:400px}
.map{left:0;top:2700px;width:1200px;height:411px;background:linear-gradient(135deg,#e9e4d8 0%,#dfe8d3 35%,#a9cbe4 55%,#e6e1d4 75%,#f1ead8 100%)}

/* others */
.avatar{left:292px;top:3226px;width:180px;height:180px;border-radius:50%;background:radial-gradient(circle at 50% 45%,#e4b99a 0%,#b9785a 55%,#6e4431 100%);border:4px solid #ddd}
.testimonial{left:173px;top:3430px;width:420px;font-size:14px;line-height:22px;color:#444}
.author{left:173px;top:3610px;font-size:14px;font-weight:700;color:var(--green)}
.date{left:405px;top:3612px;font-size:12px;color:#333}

.coupon{left:613px;top:3244px;width:419px;height:404px;border:3px solid var(--teal)}
.coupon h3{position:absolute;left:12px;top:14px;font-family:"Source Sans Pro",sans-serif;font-weight:400;font-size:46px;color:#222}
.coupon-panel{left:12px;top:78px;width:392px;height:176px;background:#e3ecef}
.coupon-text{left:14px;top:16px;width:220px;font-size:12px;line-height:18px;color:#444}
.coupon-small{left:14px;top:100px;width:220px;font-size:11px;line-height:16px;color:#666}
.off{left:248px;top:6px;width:148px;height:164px;background:#000;color:var(--white);font-family:"Source Sans Pro",sans-serif;font-weight:700;font-size:58px;line-height:62px;display:flex;flex-direction:column;justify-content:center;padding-left:12px}
.coupon-btn{left:12px;top:264px;width:392px;height:40px;background:var(--green);color:var(--white);font-size:14px;font-weight:700;display:flex;align-items:center;padding-left:10px}
.shares{left:12px;top:318px;display:flex;gap:9px}
.share{display:flex;align-items:center;gap:5px;height:26px;padding:0 8px 0 0;background:#f2f2f2;border:1px solid #ddd;font-size:11px;color:#444}
.share i{display:block;width:24px;height:24px}

.divider{left:110px;top:3689px;width:980px;height:2px;background:#aaa}

/* contact */
.contact-title{left:121px;top:3728px;font-family:"Source Sans Pro",sans-serif;font-size:50px;color:#111}
.label{font-size:14px;color:#333}
.field{background:var(--field);height:35px;width:289px}
.send{left:786px;top:4039px;width:278px;height:46px;font-size:16px;font-weight:600}

/* footer */
.footer{left:0;top:4180px;width:1200px;height:157px;background:var(--footer)}
.foot-links{left:0;width:1200px;top:32px;display:flex;justify-content:center;gap:36px;font-size:14px;color:var(--white)}
.copy{left:0;width:1200px;top:58px;text-align:center;font-size:13px;color:var(--white)}
.foot-social{left:0;width:1200px;top:90px;display:flex;justify-content:center;gap:10px}
.foot-social span{width:40px;height:40px;border-radius:50%}
</style>
</head>
<body>

<div class="abs hero" role="img" aria-label="Photo of a set restaurant table with wine glasses and a colourful salad plate"></div>
<header class="abs topbar">
  <div class="abs brand">Restaurant</div>
  <span class="abs social-top" style="left:1013px"></span>
  <span class="abs social-top" style="left:1041px"></span>
  <span class="abs social-top" style="left:1069px"></span>
</header>
<h1 class="abs hero-title">Unique &amp; Delicious Taste</h1>
<p class="abs hero-lead">Lorem ipsum dolor sit amet, consectetur adipiscing elit. Phasellus lobortis dictum elit eu placerat. Nullam vulputate tortor.</p>
<div class="abs btn-dark">
  <svg width="18" height="20" viewBox="0 0 18 20"><path d="M2 0v7a3 3 0 0 0 2 3v10h2V10a3 3 0 0 0 2-3V0H7v6H6V0H5v6H4V0z M13 0c-2 2-2 7 0 10v10h2V0z" fill="#fff"/></svg>
  <span>Read More</span>
</div>

<nav class="abs nav">
  <a style="left:330px">WELCOME</a>
  <a style="left:472px">OUR STORIES</a>
  <a style="left:628px">OUR PHOTOS</a>
  <a style="left:790px">WE WERE HERE</a>
  <a style="left:920px">BY ME</a>
  <a style="left:1020px">Home</a>
</nav>

<h2 class="abs about-title">About Our <b>Restaurant</b></h2>
<p class="abs about-sub">This is a paragraph. Writing in paragraphs lets your visitor</p>
<p class="abs about-text">This is a paragraph. Writing in paragraphs lets your visitor find what they are looking for quickly and easily. Make sure your titles stand out from the rest of the text.This is a paragraph. Writing in paragraphs lets your visitor find what they are looking for quickly and easily. Make sure your titles stand out from the rest of the text.</p>
<div class="abs btn-green find">Find a Table</div>

<div class="abs band black" style="top:1032px;height:75px">RESTAURANT&nbsp;<b>MENU</b></div>
<div class="abs menu-bg" role="img" aria-label="Faded close-up photo of a pizza with peppers and olives"></div>

<h3 class="abs cat" style="top:1117px">Appetizers</h3>
<div class="abs rule" style="top:1165px"></div>
<div class="abs item" style="left:101px;top:1210px"><div class="item-head"><span>Onion Rings</span><span>$25.00</span></div><p class="item-desc">Served with Chipotle Ranch dipping sauce. Full Order and Smaller Portion available (price varies).</p></div>
<div class="abs item" style="left:596px;top:1210px"><div class="item-head"><span>Onion Rings</span><span>$25.00</span></div><p class="item-desc">Served with Chipotle Ranch dipping sauce. Full Order and Smaller Portion available (price varies).</p></div>

<h3 class="abs cat" style="top:1380px">Main Courses</h3>
<div class="abs rule" style="top:1428px"></div>
<div class="abs item" style="left:101px;top:1473px"><div class="item-head"><span>Fresh Baked Chicken Pot Pie...</span><span>$28.00</span></div><p class="item-desc" style="width:400px">Chunks of tender, all-white chicken with carrots, onions, celery and peas in a rich cream.</p></div>
<div class="abs item" style="left:596px;top:1473px"><div class="item-head"><span>Goldbreast Turkey &amp; Dressing...</span><span>$26.00</span></div><p class="item-desc" style="width:400px">Oven-roasted and hand-carved slices, served on homestyle sage dressing with hearty turkey.</p></div>

<h3 class="abs cat" style="top:1620px">Drinks</h3>
<div class="abs rule" style="top:1668px"></div>
<div class="abs item" style="left:101px;top:1713px"><div class="item-head"><span>Lemonade</span><span>$3</span></div><p class="item-desc" style="width:400px">Made of the best lemons and sharp peppermint to provide you with the best refreshment</p></div>
<div class="abs item" style="left:596px;top:1713px"><div class="item-head"><span>Watermelon Smoothie</span><span>$4</span></div><p class="item-desc" style="width:400px">Made of the best watermelons and sweet mint to provide you with the best refreshment</p></div>

<h3 class="abs cat" style="top:1860px">Desserts</h3>
<div class="abs rule" style="top:1908px"></div>
<div class="abs item" style="left:101px;top:1953px"><div class="item-head"><span>Banana Cream</span><span>$10</span></div><p class="item-desc" style="width:400px">Seasonal ripe berries on a crispy crust with amazing smell and long-lasting aftertaste.</p></div>
<div class="abs item" style="left:596px;top:1953px"><div class="item-head"><span>Caramel Apple</span><span>$12</span></div><p class="item-desc" style="width:400px">Luscious apples with a crumb topping and rich caramel icing on a crispy crust.</p></div>

<div class="abs btn-green full-menu">View Full Menu</div>

<div class="abs band black" style="top:2174px;height:78px;font-weight:400">OUR#Gallery</div>
<div class="abs gallery-tile" style="left:0;background:linear-gradient(160deg,#d9d5cf,#6b5a4c 60%,#2c2622)" role="img" aria-label="Photo of a waiter carrying plated dishes"></div>
<div class="abs gallery-tile" style="left:400px;background:linear-gradient(180deg,#6f5a3a,#d8b978 50%,#8b6b3a)" role="img" aria-label="Photo of a pasta dish with herbs and olive oil"></div>
<div class="abs gallery-tile" style="left:800px;background:linear-gradient(135deg,#e8e2d8,#9a5a30 45%,#5c3118)" role="img" aria-label="Photo of a glazed bundt cake with white icing"></div>

<div class="abs band black" style="top:2625px;height:75px;font-weight:400">WEWERE HERE</div>
<div class="abs map" role="img" aria-label="Street map showing the restaurant location"></div>

<div class="abs band green" style="top:3111px;height:69px">Others</div>

<div class="abs avatar" role="img" aria-label="Portrait photo of a smiling guest"></div>
<p class="abs testimonial">This is a paragraph. Writing in paragraphs lets your visitor find what they are looking for quickly and easily. Make sure your titles stand out from the rest of the text. This is a paragraph. Writing in paragraphs lets your visitor find what they are looking for quickly and easily. Make sure your titles stand out from the rest of the text. This is a paragraph. Writing in paragraphs lets your visitor find what they are looking for quickly and easily. Make sure your titles stand out from the rest of the text.</p>
<div class="abs author">Ms Clara Whitfield</div>
<div class="abs date">10 March 2015 Tuesday</div>

<section class="abs coupon">
  <h3>Get A Coupon!</h3>
  <div class="abs coupon-panel">
    <p class="abs coupon-text">In here you should write the offer details. Example: get a $5 off on your next lunch order</p>
    <p class="abs coupon-small">Offer available only on lunch menu items. Offer expires Dec 29th. Not valid for drinks or special dishes.</p>
    <div class="abs off"><span>$5</span><span>OFF</span></div>
  </div>
  <div class="abs coupon-btn">Click to use coupon</div>
  <div class="abs shares">
    <span class="share"><i style="background:#3b5998"></i>Share</span>
    <span class="share"><i style="background:#29a9e1"></i>Tweet</span>
    <span class="share"><i style="background:#d34836"></i>Share</span>
    <span class="share"><i style="background:#0e76a8"></i>Share</span>
    <span class="share"><i style="background:#777"></i>Mail</span>
  </div>
</section>

<div class="abs divider"></div>

<h2 class="abs contact-title">Contact Us</h2>
<span class="abs label" style="left:136px;top:3838px">Name:</span>
<span class="abs label" style="left:454px;top:3838px">Email:</span>
<span class="abs label" style="left:775px;top:3838px">Phone:</span>
<div class="abs field" style="left:136px;top:3862px"></div>
<div class="abs field" style="left:454px;top:3862px"></div>
<div class="abs field" style="left:775px;top:3862px"></div>
<span class="abs label" style="left:136px;top:3913px">Message:</span>
<div class="abs field" style="left:136px;top:3937px;width:928px;height:76px"></div>
<div class="abs btn-green send">Send Message</div>

<footer class="abs footer">
  <div class="abs foot-links"><span>Home</span><span>About us</span><span>Menu</span><span>Gallery</span><span>Services</span><span>Contact us</span></div>
  <div class="abs copy">Copyright 2015 &nbsp; All Rights Reserved</div>
  <div class="abs foot-social">
    <span style="background:#3b5998"></span>
    <span style="background:#29a9e1"></span>
    <span style="background:#d34836"></span>
  </div>
</footer>

</body>
</html>
```